Ridgeline Build Network Inc. Letterhead

Creation of attractive and eye catching letterhead for a business start-up for the construction industry. Letterhead must relate to construction, but avoid standard hammer and tools in the design.
Updates

I forgot to add some details, sorry about that. Some pertinent info: Ph: 916-555-0148 ridgelinebuildnet.example 487 Willowmere Ave, Ste 210 Folsom, CA 95699 info@ridgelinebuildnet.example not sure if slogan should be in there" “Connecting construction professionals to create a purpose driven industry.” must be able to be used in word. Thanks!

```html
<!DOCTYPE html>
<html lang="en">
<head>
<meta charset="utf-8">
<title>Ridgeline Build Network Inc. — Letterhead</title>
<link href="https://fonts.googleapis.com/css2?family=Montserrat:wght@500;600&display=swap" rel="stylesheet">
<style>
  :root {
    --navy: #1b1e45;
    --red: #b8201f;
    --deep-red: #9c1c18;
    --paper: #ffffff;
    --backdrop: #e9edf1;
    --ghost-red: rgba(184, 32, 31, 0.08);
    --ghost-navy: rgba(27, 30, 69, 0.08);
  }
  * { box-sizing: border-box; margin: 0; padding: 0; }
  html, body { width: 1200px; height: 1200px; overflow: hidden; }
  body {
    background: var(--backdrop);
    font-family: "Montserrat", Arial, sans-serif;
    color: var(--navy);
  }
  .letterhead {
    position: absolute;
    left: 211px;
    top: 50px;
    width: 778px;
    height: 1100px;
    background: var(--paper);
    box-shadow: 0 6px 24px rgba(20, 24, 50, 0.12);
    overflow: hidden;
  }
  .brand {
    position: absolute;
    left: 52px;
    top: 58px;
    display: flex;
    align-items: center;
    gap: 10px;
  }
  .brand-mark {
    width: 14px;
    height: 14px;
    background: var(--red);
  }
  .brand-name {
    font-weight: 600;
    font-size: 15px;
    letter-spacing: 0.12em;
    text-transform: uppercase;
    color: var(--navy);
  }
  .contact {
    position: absolute;
    right: 40px;
    top: 40px;
    list-style: none;
    font-size: 13px;
    font-weight: 500;
    line-height: 22px;
    color: var(--navy);
  }
  .contact li { display: flex; align-items: center; gap: 8px; }
  .contact svg { width: 12px; height: 12px; flex: none; fill: var(--red); }
  .watermark {
    position: absolute;
    left: 0;
    right: 0;
    top: 500px;
    text-align: center;
    font-weight: 500;
    font-size: 38px;
    letter-spacing: 0.1em;
    text-transform: uppercase;
    color: var(--ghost-navy);
  }
  .watermark-rule {
    position: absolute;
    left: 170px;
    right: 170px;
    top: 565px;
    height: 2px;
    background: var(--ghost-red);
  }
  .skyline {
    position: absolute;
    left: 0;
    right: 0;
    bottom: 20px;
    height: 100px;
    background: linear-gradient(180deg, rgba(27,30,69,0) 0%, rgba(27,30,69,0.35) 25%, var(--navy) 70%);
  }
  .base-band {
    position: absolute;
    left: 0;
    right: 0;
    bottom: 0;
    height: 20px;
    background: var(--deep-red);
  }
</style>
</head>
<body>
  <main class="letterhead">
    <header class="brand">
      <span class="brand-mark"></span>
      <span class="brand-name">Ridgeline Build Network Inc.</span>
    </header>

    <ul class="contact">
      <li>
        <svg viewBox="0 0 12 12" aria-hidden="true"><rect x="0" y="0" width="12" height="12" rx="2"/><path d="M3.2 2.6l1.4 0 .6 1.8-.9.7a5 5 0 0 0 2.6 2.6l.7-.9 1.8.6 0 1.4c-3.4.3-6.5-2.8-6.2-6.2z" fill="#fff"/></svg>
        916-555-0148
      </li>
      <li>
        <svg viewBox="0 0 12 12" aria-hidden="true"><rect x="0" y="1.5" width="12" height="9" rx="1.5"/><path d="M1.5 3l4.5 3.3L10.5 3" stroke="#fff" stroke-width="1.2" fill="none"/></svg>
        info@ridgelinebuildnet.example
      </li>
      <li>
        <svg viewBox="0 0 12 12" aria-hidden="true"><path d="M6 0a4.2 4.2 0 0 0-4.2 4.2C1.8 7.3 6 12 6 12s4.2-4.7 4.2-7.8A4.2 4.2 0 0 0 6 0zm0 6a1.7 1.7 0 1 1 0-3.4A1.7 1.7 0 0 1 6 6z"/></svg>
        487 Willowmere Ave, Ste 210, Folsom, CA 95699
      </li>
      <li>
        <svg viewBox="0 0 12 12" aria-hidden="true"><circle cx="6" cy="6" r="6"/><path d="M0.5 6h11M6 0.5c-2.4 3-2.4 8 0 11M6 0.5c2.4 3 2.4 8 0 11" stroke="#fff" stroke-width="0.9" fill="none"/></svg>
        ridgelinebuildnet.example
      </li>
    </ul>

    <div class="watermark">Ridgeline Build Network Inc.</div>
    <div class="watermark-rule"></div>

    <div class="skyline" role="img" aria-label="Navy and red city skyline silhouette with tower cranes and buildings under construction"></div>
    <div class="base-band"></div>
  </main>
</body>
</html>
```